Elevating our current Business Card Design

We want to elevate our current business card with a new design to look like a marlow 800 company. We are a premium lubricant distributor (oil and grease).
We need 2 versions, version 1 is as per the uploaded a copy of our current business card with the English version.
For our Chinese version we need to use the front to be English in English and have the back of the card designed exactly like the front for all info to be in Chinese.
The design template needs to be such that we can amend the template with adding different information for each person's card.
The background colour of the card can be changed- we just need to clearly see all information on the card and logos.
The TRV and Verdant Mark logos cannot have any colour or display changes- only use the logos attached.
All logos need to be included and all information from the attached current card

```html
<!DOCTYPE html>
<html lang="en">
<head>
<meta charset="UTF-8">
<title>NLX Business Card</title>
<link rel="stylesheet" href="https://fonts.googleapis.com/css2?family=Montserrat:wght@400;500;700;800&display=swap">
<style>
  :root {
    --stage: #1c1c1c;
    --card-white: #ffffff;
    --card-black: #050505;
    --brand-red: #ec2b24;
    --band-grey: #d4d4d6;
    --ink: #1f1f1f;
    --badge-green: #1f4d3a;
    --badge-grey: #6e6e70;
  }
  * { margin: 0; padding: 0; box-sizing: border-box; }
  html, body { width: 1200px; height: 1059px; overflow: hidden; }
  body {
    background: var(--stage);
    font-family: "Montserrat", Arial, sans-serif;
    position: relative;
  }
  .card { position: absolute; border-radius: 24px; overflow: hidden; }

  /* Front */
  .card-front { left: 257px; top: 86px; width: 688px; height: 394px; background: var(--card-white); }
  .front-wave { position: absolute; left: 0; top: 0; width: 688px; height: 394px; }
  .front-brand {
    position: absolute; left: 60px; top: 140px; width: 300px; text-align: center;
    font-weight: 800; font-size: 72px; color: var(--brand-red); letter-spacing: 2px; line-height: 1;
  }
  .front-divider { position: absolute; left: 348px; top: 89px; width: 2px; height: 172px; background: var(--brand-red); }
  .person-name { position: absolute; left: 375px; top: 82px; font-size: 24px; font-weight: 800; color: var(--brand-red); line-height: 1.2; }
  .person-role { position: absolute; left: 375px; top: 112px; font-size: 14px; font-weight: 500; color: var(--ink); }
  .contact-list { position: absolute; left: 374px; top: 143px; list-style: none; }
  .contact-list li { display: flex; align-items: center; height: 24px; font-size: 15px; color: var(--ink); }
  .contact-list svg { width: 17px; height: 17px; margin-right: 15px; flex: none; fill: var(--brand-red); }
  .address { position: absolute; left: 68px; top: 333px; font-size: 15px; line-height: 18px; color: #fff; }

  /* Back */
  .card-back { left: 253px; top: 545px; width: 707px; height: 402px; background: var(--card-black); }
  .back-brand {
    position: absolute; left: 0; top: 70px; width: 707px; text-align: center;
    font-weight: 800; font-size: 150px; color: var(--brand-red); letter-spacing: 6px; line-height: 1;
  }
  .partner-badge { position: absolute; }
  .badge-verdant { left: 24px; top: 268px; width: 135px; height: 100px; border-radius: 6px; background: var(--badge-green); }
  .badge-lockup { left: 173px; top: 307px; width: 338px; height: 53px; border-radius: 6px; background: var(--brand-red); }
  .badge-trv { left: 540px; top: 258px; width: 124px; height: 124px; border-radius: 50%; background: var(--badge-grey); }
</style>
</head>
<body>

<section class="card card-front">
  <svg class="front-wave" viewBox="0 0 688 394" aria-hidden="true">
    <path d="M0 290 C40 282 70 278 96 279 C250 282 380 352 502 352 C600 352 660 300 688 278 L688 394 L0 394 Z" fill="var(--band-grey)"/>
    <path d="M0 296 C40 288 70 284 96 284 C250 290 380 366 502 366 C600 366 660 330 688 307 L688 394 L0 394 Z" fill="var(--brand-red)"/>
  </svg>

  <div class="front-brand">NLX</div>
  <div class="front-divider"></div>

  <h1 class="person-name">Clara Vennet</h1>
  <p class="person-role">Administraction Executive</p>

  <ul class="contact-list">
    <li><svg viewBox="0 0 20 20"><path d="M2 7c0-3 4-4 8-4s8 1 8 4v2h-4V7H6v2H2z"/><path d="M5 10h10l1 8H4z"/><circle cx="10" cy="14" r="2" fill="#fff"/></svg>1300 000 472</li>
    <li><svg viewBox="0 0 20 20"><path d="M6 1h8a1 1 0 0 1 1 1v16a1 1 0 0 1-1 1H6a1 1 0 0 1-1-1V2a1 1 0 0 1 1-1zm1 2v12h6V3z"/></svg>+16 400 000 118</li>
    <li><svg viewBox="0 0 20 20"><path d="M5 2h10v4H5z"/><path d="M2 7h16v7h-3v-3H5v3H2z"/><path d="M6 12h8v6H6z"/></svg>+16 8 9000 2245</li>
    <li><svg viewBox="0 0 20 20"><path d="M1 4h18v12H1z"/><path d="M1 4l9 7 9-7" fill="none" stroke="#fff" stroke-width="1.5"/></svg>clara.vennet@nlxdirect.com</li>
    <li><svg viewBox="0 0 20 20"><circle cx="10" cy="10" r="9"/><path d="M5 6c2 0 3 2 2 4s-2 3-1 5M12 3c0 3 3 3 3 6s-2 4-1 7" fill="none" stroke="#fff" stroke-width="1.4"/></svg>www.nlxdirect.com</li>
  </ul>

  <p class="address">48 Harbour Freight Way<br>Ashdale, WA 6190</p>
</section>

<section class="card card-back">
  <div class="back-brand">NLX</div>

  <div class="partner-badge badge-verdant" role="img" aria-label="Verdant Mark network member badge"></div>
  <div class="partner-badge badge-lockup" role="img" aria-label="Northline Lubricant Exchange and Meridian Oils premium lubricants partner badge"></div>
  <div class="partner-badge badge-trv" role="img" aria-label="TRV ISO 45001 system certification badge"></div>
</section>

</body>
</html>
```